KDR Business Card

Keystone Draper Resources is a successful and reputable financial services company.Our main services are home loans, commercial loans, vehicle finance and equipment finance. We also do development finance for property developers. Our company is always evolving to always be an industry leader in best financial service practices with access to the largest range of lenders in the country.

We want the business card to reflect our national finance company. Modern, professional corporate image. At the same time the concept of Keystone Draper Resources is that we help build wealth for you but the process for the client is an enjoyable peaceful experience. Not stressful at all .....

Colors to be same as the logo .... gold silver black white as the options

On the reverse side of the card I wanted either just the logo symbol or the logo symbol and text of the logo ....

It could be on a black background ..... or silver or gold .... want it to be quite striking to look at when you first see the card.

On the other side of the card I wanted the following details:

Martin Haldane
Director

0438 927 604

martin@kdrgrp.com.au

Po Box 718
Ferndale ACT 2614

www.kdrgrp.com.au

ACN 618 204 957 (This can be in very small print and can be in the bottom corner of the card or somewhere not very prominent)

As requested Ive uploaded the logo file in both .ai and .pdf formats. Please let me know if you need anything else. Thanks

Reason: Still deciding on which design I like best. I will provide individual feedback as well.

```html
<!DOCTYPE html>
<html lang="en">
<head>
<meta charset="utf-8">
<title>KDR Business Card</title>
<link href="https://fonts.googleapis.com/css2?family=Cinzel:wght@400;600&family=Lato:wght@300;400&display=swap" rel="stylesheet">
<style>
  :root {
    --backdrop: #e9e6e1;
    --card-white: #ffffff;
    --card-mist: #eceff1;
    --ink-black: #1e1e1f;
    --ink-charcoal: #2b2b2c;
    --gold: #c9a94a;
    --gold-light: #e2c978;
    --silver: #8f9296;
    --text-light: #e9e9e9;
  }
  * { box-sizing: border-box; margin: 0; padding: 0; }
  html, body { width: 1200px; height: 1000px; overflow: hidden; }
  body {
    background: var(--backdrop);
    display: flex;
    flex-direction: column;
    align-items: center;
    justify-content: center;
    gap: 40px;
    font-family: "Lato", sans-serif;
  }
  .card {
    position: relative;
    width: 800px;
    height: 457px;
    border-radius: 22px;
    overflow: hidden;
    box-shadow: 0 10px 30px rgba(0,0,0,0.18);
  }

  /* Front */
  .card-front {
    background: radial-gradient(ellipse at 60% 30%, var(--card-white) 0%, var(--card-mist) 100%);
  }
  .front-watermark {
    position: absolute;
    left: -70px;
    bottom: -110px;
    width: 340px;
    height: 340px;
    border-radius: 50%;
    background: var(--gold-light);
    opacity: 0.12;
  }
  .front-brand {
    position: absolute;
    right: 60px;
    top: 50%;
    transform: translateY(-50%);
    text-align: right;
    font-family: "Cinzel", serif;
    font-weight: 400;
    color: var(--gold);
    font-size: 40px;
    line-height: 1.15;
    letter-spacing: 2px;
  }

  /* Back */
  .card-back { background: var(--card-white); }
  .back-bands { position: absolute; inset: 0; }
  .back-details {
    position: absolute;
    left: 56px;
    top: 58px;
    width: 380px;
    color: var(--text-light);
  }
  .holder-name {
    font-family: "Cinzel", serif;
    font-weight: 400;
    font-size: 34px;
    color: var(--gold);
    letter-spacing: 1px;
  }
  .holder-rule {
    width: 150px;
    height: 1px;
    background: var(--gold);
    margin: 12px 0 10px;
  }
  .holder-title {
    font-size: 13px;
    letter-spacing: 4px;
    text-transform: uppercase;
    color: var(--text-light);
  }
  .contact-list {
    list-style: none;
    margin-top: 36px;
    display: flex;
    flex-direction: column;
    gap: 14px;
    font-size: 16px;
    font-weight: 300;
  }
  .contact-list li { display: flex; align-items: flex-start; gap: 14px; line-height: 1.35; }
  .contact-icon { width: 18px; height: 18px; flex: none; margin-top: 1px; }
  .company-number {
    position: absolute;
    left: 56px;
    bottom: 26px;
    font-size: 10px;
    letter-spacing: 1.5px;
    color: var(--silver);
  }
  .back-brand {
    position: absolute;
    right: 44px;
    top: 50%;
    transform: translateY(-50%);
    width: 170px;
    text-align: right;
    font-family: "Cinzel", serif;
    font-weight: 400;
    color: var(--gold);
    font-size: 24px;
    line-height: 1.2;
    letter-spacing: 1.5px;
  }
</style>
</head>
<body>

  <section class="card card-front" aria-label="Card front">
    <div class="front-watermark" aria-hidden="true"></div>
    <div class="front-brand">Keystone Draper<br>Resources</div>
  </section>

  <section class="card card-back" aria-label="Card back">
    <svg class="back-bands" viewBox="0 0 800 457" preserveAspectRatio="none" aria-hidden="true">
      <polygon points="0,0 470,0 560,457 0,457" fill="var(--ink-black)"/>
      <polygon points="476,0 484,0 574,457 566,457" fill="var(--card-white)"/>
      <polygon points="484,0 494,0 584,457 574,457" fill="var(--ink-charcoal)"/>
      <polygon points="494,0 501,0 591,457 584,457" fill="var(--card-white)"/>
      <polygon points="501,0 510,0 600,457 591,457" fill="var(--ink-charcoal)"/>
    </svg>

    <div class="back-details">
      <h1 class="holder-name">Martin Haldane</h1>
      <div class="holder-rule"></div>
      <p class="holder-title">Director</p>

      <ul class="contact-list">
        <li>
          <svg class="contact-icon" viewBox="0 0 24 24" fill="var(--gold)"><path d="M6.6 10.8a15.1 15.1 0 0 0 6.6 6.6l2.2-2.2a1 1 0 0 1 1-.25 11.4 11.4 0 0 0 3.6.57 1 1 0 0 1 1 1V20a1 1 0 0 1-1 1A17 17 0 0 1 3 4a1 1 0 0 1 1-1h3.5a1 1 0 0 1 1 1c0 1.25.2 2.45.57 3.6a1 1 0 0 1-.25 1z"/></svg>
          <span>0438 927 604</span>
        </li>
        <li>
          <svg class="contact-icon" viewBox="0 0 24 24" fill="none" stroke="var(--gold)" stroke-width="1.8"><rect x="3" y="5" width="18" height="14" rx="1.5"/><path d="M3 6l9 7 9-7"/></svg>
          <span>martin@kdrgrp.com.au</span>
        </li>
        <li>
          <svg class="contact-icon" viewBox="0 0 24 24" fill="var(--gold)"><path d="M12 2a7 7 0 0 0-7 7c0 5.2 7 13 7 13s7-7.8 7-13a7 7 0 0 0-7-7zm0 9.5A2.5 2.5 0 1 1 12 6.5a2.5 2.5 0 0 1 0 5z"/></svg>
          <span>Po Box 718<br>Ferndale ACT 2614</span>
        </li>
        <li>
          <svg class="contact-icon" viewBox="0 0 24 24" fill="none" stroke="var(--gold)" stroke-width="1.6"><circle cx="12" cy="12" r="9"/><path d="M3 12h18M12 3c3 3.2 3 14.8 0 18M12 3c-3 3.2-3 14.8 0 18"/></svg>
          <span>www.kdrgrp.com.au</span>
        </li>
      </ul>
    </div>

    <p class="company-number">ACN 618 204 957</p>

    <div class="back-brand">Keystone<br>Draper<br>Resources</div>
  </section>

</body>
</html>
```